Business Brochure / White Paper

This white paper is a marketing document to showcase ourselves to other businesses (private hospitals and other premium healthcare providers). The document should consist of bold and beautiful graphics. As an example of the sort of thing that we mean, we have attached the "velmora sky lineage records" white paper. It should consist of several A4 pages.
The content for the white paper is attached. Note that the content document is only a scaffold for the white paper and the exact layout does not need to be followed (especially text boxes which have just been placed roughly). You are free to use your artistic license to move content around in order to make the document as catchy as possible.
We have also included graphics that we have purchased licenses to and that we encourage to be used as you see fit. Note that in some places we have added a note after two asterisks (i.e. **) when we would like you to add specific images/graphics.
All of the relevant documents and graphics/images to be used to make the white paper can be found at the below link:
https://www.filquarry.net/sh/zhtwmekbb41paxl/BBDN5K3TB8FWLPNTq1tGmeOWRc?dl=0
Feel free to ask any questions.
Good Luck!
Hi,
Thank you for your submissions so far.
Please use our dropbox link for an updated and much more specific brief on what we require in terms of content, layout, and components:
Please note that we must make a decision within 3 days' time.
Please also note that we cannot select a designer unless designs for ALL PAGES of the white paper are submitted.
Thank you and good luck!

```html
<!DOCTYPE html>
<html lang="en">
<head>
<meta charset="utf-8">
<title>Precision Medicine – Spread</title>
<link rel="stylesheet" href="https://fonts.googleapis.com/css2?family=Baskervville:ital@0;1&family=Playfair+Display:ital,wght@1,400&display=swap">
<style>
  :root {
    --navy: #2b3990;
    --green: #62b046;
    --paper: #ffffff;
    --photo-light: #e4ecf4;
    --photo-mid: #7ea4cf;
    --photo-deep: #2f5c9c;
  }
  * { margin: 0; padding: 0; box-sizing: border-box; }
  html, body { width: 1200px; height: 848px; overflow: hidden; background: var(--paper); }
  .spread { position: relative; width: 1200px; height: 848px; background: var(--paper); overflow: hidden; }
  .page { position: absolute; top: 0; height: 848px; }
  .page--left { left: 0; width: 608px; }
  .page--right { left: 608px; width: 592px; }

  .title-rule { position: absolute; left: 58px; top: 88px; width: 33px; height: 3px; background: var(--green); }
  .title {
    position: absolute; left: 56px; top: 86px;
    font-family: "Playfair Display", serif; font-style: italic; font-weight: 400;
    font-size: 54px; letter-spacing: -0.5px; color: var(--navy); white-space: nowrap;
  }
  .title .accent { color: var(--green); }

  .body-copy {
    position: absolute; left: 58px; top: 236px; width: 425px;
    font-family: "Baskervville", serif; font-size: 10.4px; line-height: 14.5px; color: var(--navy);
  }
  .body-copy p { margin-bottom: 14.5px; }

  .benefits { position: absolute; top: 92px; left: 50px; display: flex; gap: 9px; }
  .benefit { width: 82px; text-align: center; }
  .benefit svg { width: 38px; height: 40px; display: block; margin: 0 auto; }
  .benefit-rule { height: 1px; background: var(--green); margin: 6px 0 8px; }
  .benefit-label {
    font-family: "Baskervville", serif; font-style: italic; font-size: 10px; line-height: 14px;
    text-transform: uppercase; color: var(--navy);
  }

  .did-you-know {
    position: absolute; left: 50px; top: 232px;
    font-family: "Playfair Display", serif; font-style: italic; font-weight: 400; font-size: 27px; color: var(--navy);
  }
  .fact {
    position: absolute; left: 50px; top: 278px; width: 488px;
    font-family: "Baskervville", serif; font-size: 10.4px; line-height: 14.5px; color: var(--navy);
  }
  .gradient-bar {
    position: absolute; left: 50px; top: 341px; width: 486px; height: 5px;
    background: linear-gradient(90deg, var(--navy) 0%, var(--navy) 35%, var(--green) 100%);
  }
  .quote {
    position: absolute; left: 50px; top: 360px; width: 490px;
    font-family: "Playfair Display", serif; font-style: italic; font-weight: 400; font-size: 13.6px; line-height: 20px; color: var(--navy);
  }
  .attribution {
    position: absolute; left: 50px; top: 498px; width: 300px;
    font-family: "Baskervville", serif; font-style: italic; font-size: 11px; line-height: 14px; color: var(--green);
  }

  .team-photo {
    position: absolute; left: 500px; top: 560px; width: 700px; height: 288px;
    background: linear-gradient(180deg, rgba(228,236,244,0) 0%, var(--photo-light) 18%, var(--photo-mid) 55%, var(--photo-deep) 100%);
    border-top-left-radius: 60px;
  }
</style>
</head>
<body>
<main class="spread">
  <section class="page page--left">
    <div class="title-rule"></div>
    <h1 class="title"><span class="accent">Precision</span> Medicine</h1>
    <div class="body-copy">
      <p>The Harrowgate Clinic, Linden Hale Hospital, Brookmere Clinic and Eastvale General Hospital. These are just some of the world’s most reputable medical clinics that are already offering genomic and precision healthcare to their patients. Premium healthcare providers around the world, including private hospitals, high-end primary care practices, executive health providers and concierg The Harrowgate Clinic, Linden Hale Hospital, Brookmere Clinic and Eastvale General Hospital. These are just some of the world’s most reputable medical clinics that are already offering genomic and precision healthcare to their patients. Premium healthcare providers around the world, including private hospitals, high-end primary care practices, executive health providers and concierge medicine clinics, are rapidly following suit.</p>
      <p>Ever since the human genome was decoded, a plethora of scientific research has been compiled and the amount of new research and actionable data has grown at an exponential rate. The science has been moving much faster than industry can keep up with but precision medicine is now quickly becoming mainstream practise. The revolution has begun and genomic-driven precision medicine is set to become the new standard in healthcare delivery.</p>
      <p>GenorraTM partners with premium health providers like you to take yout business to the next level and set you apart from competitors. Our cutting-edge products allow you to offer the same in world-class precision and genomic healthcare. The science is clear, the technology is ready, and the time for clinical implementation is now. e medicine clinics, are rapidly following suit.</p>
      <p>Ever since the human genome was decoded, a plethora of scientific research has been compiled and the amount of new research and actionable data has grown at an exponential rate. The science has been moving much faster than industry can keep up with but precision medicine is now quickly becoming mainstream practise. The revolution has begun and genomic-driven precision medicine is set to become the new standard in healthcare delivery.</p>
      <p>GenorraTM partners with premium health providers like you to take yout business to the next level and set you apart from competitors. Our cutting-edge products allow you to offer the same in world-class precision and genomic healthcare. The science is clear, the technology is ready, and the time for clinical implementation is now.</p>
    </div>
  </section>

  <section class="page page--right">
    <div class="benefits">
      <div class="benefit">
        <svg viewBox="0 0 38 40" aria-hidden="true">
          <rect x="8" y="6" width="22" height="30" rx="2" fill="none" stroke="var(--navy)" stroke-width="2.5"/>
          <rect x="14" y="3" width="10" height="6" rx="1" fill="var(--navy)"/>
          <polyline points="11,23 16,23 18,18 21,28 23,23 27,23" fill="none" stroke="var(--green)" stroke-width="1.8"/>
        </svg>
        <div class="benefit-rule"></div>
        <div class="benefit-label">Improve<br>Patient<br>Care</div>
      </div>
      <div class="benefit">
        <svg viewBox="0 0 38 40" aria-hidden="true">
          <path d="M19 34 C8 26 3 20 3 13 C3 8 7 5 11 5 C15 5 17 7 19 10 C21 7 23 5 27 5 C31 5 35 8 35 13 C35 20 30 26 19 34 Z" fill="none" stroke="var(--navy)" stroke-width="2.3"/>
          <polyline points="1,19 12,19 15,14 19,25 22,17 24,19 37,19" fill="none" stroke="var(--green)" stroke-width="1.8"/>
        </svg>
        <div class="benefit-rule"></div>
        <div class="benefit-label">Increase<br>Therapy<br>Effectiveness</div>
      </div>
      <div class="benefit">
        <svg viewBox="0 0 38 40" aria-hidden="true">
          <rect x="8" y="4" width="22" height="32" fill="none" stroke="var(--navy)" stroke-width="2.3"/>
          <path d="M14 9 h3 v-2 h2 v2 h3 v2 h-3 v2 h-2 v-2 h-3 z" fill="var(--green)"/>
          <line x1="12" y1="19" x2="26" y2="19" stroke="var(--navy)" stroke-width="1.5"/>
          <line x1="12" y1="23" x2="26" y2="23" stroke="var(--navy)" stroke-width="1.5"/>
          <line x1="12" y1="27" x2="26" y2="27" stroke="var(--navy)" stroke-width="1.5"/>
          <line x1="12" y1="31" x2="22" y2="31" stroke="var(--navy)" stroke-width="1.5"/>
        </svg>
        <div class="benefit-rule"></div>
        <div class="benefit-label">Limit<br>Adverse<br>Outcomes</div>
      </div>
      <div class="benefit">
        <svg viewBox="0 0 38 40" aria-hidden="true">
          <path d="M12 6 h10 v10 h10 v10 h-10 v10 h-10 v-10 h-10 v-10 h10 z" fill="var(--navy)"/>
          <polyline points="15,22 21,29 36,10" fill="none" stroke="var(--paper)" stroke-width="5"/>
          <polyline points="15,22 21,29 36,10" fill="none" stroke="var(--green)" stroke-width="2.5"/>
        </svg>
        <div class="benefit-rule"></div>
        <div class="benefit-label">Improve<br>Medical<br>Compliance</div>
      </div>
      <div class="benefit">
        <svg viewBox="0 0 38 40" aria-hidden="true">
          <circle cx="20" cy="20" r="16" fill="none" stroke="var(--navy)" stroke-width="2.3"/>
          <polyline points="1,21 12,21 15,15 19,28 22,18 24,21 32,21" fill="none" stroke="var(--green)" stroke-width="1.8"/>
        </svg>
        <div class="benefit-rule"></div>
        <div class="benefit-label">Improve<br>Economic<br>Efficiency</div>
      </div>
    </div>

    <h2 class="did-you-know">Did You Know?</h2>
    <p class="fact">Response rates for many prescribed drugs are as low as 50% and that genetic factors can account for up to 95% of drug-response variability and susceptibility!2,3 That’s why physicians are turning to precision prescribing!</p>
    <div class="gradient-bar"></div>
    <blockquote class="quote">“Doctors have always recognized that every patient is unique, and doctors have always tried to tailor their treatments as best they can to individuals. You can match a blood transfusion to a blood type — that was an important discovery. What if matching a cancer cure to our genetic code was just as easy, just as standard? What if figuring out the right dose of medicine was as simple as taking our temperature?”</blockquote>
    <p class="attribution">- President Alder Voss,<br>At the announcement of a $215 Million<br>Precision-Medicine Genetic Plan,<br>January 30, 2015.1</p>
  </section>

  <div class="team-photo" role="img" aria-label="Photograph of a group of doctors and nurses in white coats and blue scrubs standing in a row"></div>
</main>
</body>
</html>
```